Tri-fold Brochure Design for Law Firm

I need a tri-fold brochure to give to prospective clients.
I have attached a Photoshop design file of a tri-fold brochure. The content (copy) is good, however, he brochure itself looks very amateurish.
I want a professional, sophisticated looking brochure.
The law firm specializes in commercial debt collection.
The law firm is located in New York City.
Our target market is business owners, doctors, lawyers, collection agencies and accountants.
Visit my website which is being designed at www.dorvenlaw.com. I like the font used for the name of my company and the rich blue color used.

Target Market(s)

Business Owners, Doctors, Law Firms and Accountants

Industry/Entity Type

Law Firm

Font styles to use
Serif

Requirements
Must have
• Professional quality graphic work. Attention to details.
• PHOTOGRAPHS ONLY, NO CLIP-ART.
• DARK COLORS - NAVY BLUE, HUNTER GREEN, BLACK, GRAY & WHITE
Nice to have
• I want it to look smart, modern and sophisticated.
• Visit my website which is being designed at www.dorvenlaw.com. I like the font used for the name of my company and the rich blue color used.
Should not have
• Bad artwork
• CLIP ART

```html
<!DOCTYPE html>
<html lang="en">
<head>
<meta charset="utf-8">
<title>Dorven &amp; Associates – Tri-fold Brochure</title>
<link href="https://fonts.googleapis.com/css2?family=Roboto+Condensed:wght@300;400&family=Roboto:ital,wght@0,300;0,400;1,300&display=swap" rel="stylesheet">
<style>
  :root{
    --navy:#0c4d9c;
    --green:#12a48a;
    --ice:#e2f0fa;
    --white:#ffffff;
    --ink:#1d1d1f;
  }
  html,body{margin:0;padding:0;overflow:hidden;background:var(--white);}
  .brochure{
    position:relative;width:1200px;height:927px;overflow:hidden;
    font-family:"Roboto",Arial,sans-serif;font-weight:300;
    font-size:16.4px;line-height:21px;color:var(--white);
  }
  .backdrop{position:absolute;inset:0;}
  .block{position:absolute;}
  .block h2{
    margin:0 0 10px;font-family:"Roboto Condensed",Arial,sans-serif;font-weight:300;
    font-size:31px;line-height:34px;letter-spacing:.5px;text-transform:uppercase;
  }
  .block p{margin:0 0 11px;text-align:justify;}
  .left{left:28px;width:337px;}
  .mid{left:418px;width:353px;}
  .right{left:815px;width:365px;}
  .on-white,.on-white h2{color:var(--navy);}
  .dark{color:var(--ink);}
  .dark h2{color:var(--ink);font-size:24px;line-height:28px;margin-bottom:12px;}
  .right h2.centered{text-align:center;font-size:26px;line-height:30px;}
  .on-ice{color:var(--ink);}
  .firm-name{font-style:italic;margin:0 0 4px !important;text-align:left !important;}
  .lead{font-size:18.5px;font-weight:400;margin:0 0 3px !important;text-align:left !important;}
  .fees{display:flex;margin:0;}
  .fees ul{margin:0;padding:0;list-style:none;}
  .fees li::before{content:"• ";}
  .fees span{margin-right:8px;}
</style>
</head>
<body>
<main class="brochure">
  <svg class="backdrop" width="1200" height="927" viewBox="0 0 1200 927">
    <defs>
      <linearGradient id="photoTone" x1="0" y1="0" x2="1" y2="1">
        <stop offset="0" stop-color="#8aa6cb"/>
        <stop offset=".45" stop-color="#dbe4ee"/>
        <stop offset=".75" stop-color="#c49a78"/>
        <stop offset="1" stop-color="#eef2f6"/>
      </linearGradient>
      <linearGradient id="cashTone" x1="0" y1="0" x2="1" y2="1">
        <stop offset="0" stop-color="#c9d3b8"/>
        <stop offset="1" stop-color="#e0b49a"/>
      </linearGradient>
    </defs>
    <rect width="1200" height="927" fill="var(--navy)"/>
    <rect role="img" aria-label="Photo of a stethoscope on medical paperwork, a gavel on a law block and a business handshake"
          x="393" y="238" width="400" height="270" fill="url(#photoTone)"/>
    <path d="M0,168 Q260,160 470,235 Q560,270 393,262 L393,290 Q560,330 690,420 Q760,470 797,500 L797,927 L0,927 Z" fill="var(--white)"/>
    <path d="M0,168 Q260,160 393,205 L393,262 Q300,230 0,230 Z" fill="var(--white)"/>
    <path d="M0,178 Q260,172 393,214" fill="none" stroke="var(--green)" stroke-width="10"/>
    <path d="M0,508 Q310,495 393,590 L393,927 L0,927 Z" fill="var(--green)"/>
    <path d="M735,372 Q800,405 830,476 L797,657 Q790,540 725,478 Z" fill="var(--green)"/>
    <rect x="797" y="476" width="403" height="181" fill="var(--green)"/>
    <rect x="797" y="657" width="403" height="270" fill="var(--ice)"/>
    <rect role="img" aria-label="Photo of a hand holding a bundle of dollar bills"
          x="88" y="764" width="232" height="163" rx="8" fill="url(#cashTone)"/>
  </svg>

  <section class="block left" style="top:22px">
    <h2>Who We Are</h2>
    <p class="firm-name">DORVEN &amp; ASSOCIATES, PLLC ('DORVEN')</p>
    <p>is a New York based law firm devoted to the collection of accounts receivable and business debts.</p>
  </section>

  <section class="block left on-white" style="top:210px">
    <h2>What We Do</h2>
    <p>Within 24 to 72 hours of receiving a claim, we will verify the debt, investigate the Debtor, skip trace all known stakeholders and file a lawsuit with the intent of collecting the full amount due in the shortest time possible.</p>
    <p>We will use all legal means necessary to locate, identify, seize, or otherwise garnish a Debtor's assets and income, while always having an attorney available to speak directly with the Debtor to achieve an amicable resolution as quickly as possible.</p>
  </section>

  <section class="block left" style="top:543px">
    <h2>Our Mission</h2>
    <p>Our mission is to protect our clients' bottom line, while preserving their reputation.</p>
    <p>We recognize and appreciate that your Debtor was once a trusted customer and may be a source of future revenue.</p>
    <p>We treat all Debtors with respect, while aggressively seeking to collect all monies owed.</p>
  </section>

  <section class="block mid" style="top:22px">
    <h2>Flexible Fee Structure</h2>
    <p style="margin:0">We recognize that each claim is unique, therefore to better serve our clients we offer a variety of fee structures that meet the needs of our clients.</p>
    <div class="fees"><span>Including:</span>
      <ul>
        <li>Contingency Fee</li>
        <li>Flat Fee</li>
        <li>Hourly fee</li>
        <li>Monthly or Annual Retainer</li>
        <li>Any combination of the above</li>
      </ul>
    </div>
  </section>

  <section class="block mid dark" style="top:507px">
    <h2>Handling Medical Receivables</h2>
    <p>Medical receivables require a soft touch.</p>
    <p>Doctors and health organizations often write-off tens of thousands of dollars in unpaid deductibles and co-insurance which are rightfully due them out of fear that pursuing these debts will alienate, upset or offend their patients.</p>
    <p>We offer non-legal, HIPAA compliant collection methods which can effectively and consistently turn these otherwise uncollectible assets into real cash.</p>
    <p>Using a combination of letters and phone calls, our staff contacts patients in a professional and friendly manner to arrange for payments, as small as $15 per month, encouraging them to pay all monies owed.</p>
  </section>

  <section class="block right" style="top:22px">
    <h2 class="centered">Credit Advisory Services</h2>
    <p class="lead">How well do you really know your customers?</p>
    <p>As an added service to all of our clients, we will draft a customized credit application to be distributed to all of their customers.</p>
    <p>Working closely and alongside their salespeople, we will discretely review and verify the customers' information and investigate all known stakeholders in order to determine creditworthiness.</p>
    <p style="margin:0">As your credit advisor, we will then make a meaningful recommendation with regard to the amount and terms credit should be offered to specific customers.</p>
    <p>Once a credit determination is made, we can provide the client with a credit agreement detailing each parties' obligations. Using such agreements minimizes risk, while enhancing our clients' professional stature with their customers.</p>
  </section>

  <section class="block right" style="top:487px">
    <h2 class="centered">Keeping You in Compliance</h2>
    <p>As your collection attorney and advisor, we will assure that your collection practices are in full compliance with all applicable Federal and State laws, including The Fair Debt Collection Practices Act (FDCPA) and The Health Insurance Portability and Accountability Act (HIPAA).</p>
  </section>

  <section class="block right on-ice" style="top:668px">
    <h2 class="centered">State-of-the Art Technology</h2>
    <p>Our firm prides itself on utilizing the state-of-the-art technology in law office management, telephony, cyber security, document production, and cloud storage.</p>
    <p>Our clients can be assured that their critical business data is stored in a safe, secure, and confidential environment, while allowing us to seamlessly handle a large and ever growing book of business in a timely manner.</p>
  </section>
</main>
</body>
</html>
```